upmarket hair salon Double sided design flyer/A1 poster

Address
BRENWOOD STORE Shop 8/2 Marlowen Pde Brenwood 6091
Brenwood phone 9517 3086
TALLOWMERE STORE Shop 6/41 Corvella Dunes Ave Tallowmere 6094
Tallowmere 9538 2470
Specials
NEW Clients
Try out Silken Tressa Studio
Cut and Blow-dry
$40
Elegance Package
1/2 head of foils
or root-retouch, Cut and Blow-dry
$120*
Luxurious Package
Global Colour,Treatment,
Cut and Blow-dry
$159*
Royal Pamper Package
Colour, Foils, Treatment,
Cut and Blow-dry
$220*
*packages do not include Toners
Lavish Event Package
Event hair styling and Makeup
starting From $159
a actual Tear Off section so they can cut it out
Refer A Friend that has not been to Silken Tressa and
both Receive $20 OFF your next Colour Package
Must have the phone numbers addresses that would be in the tear of sections
Design style like
Professional
upmarket
Domask pattern
blacks whites silvers maybe gold?
colours which are in logo
if any pics must have good hair and not trashy looking girls
This is the basics will give more updates if needed

```html
<!DOCTYPE html>
<html lang="en">
<head>
<meta charset="utf-8">
<title>Silken Tressa Studio – Specials Flyer</title>
<link href="https://fonts.googleapis.com/css2?family=Oswald:wght@300;400;600&family=Parisienne&display=swap" rel="stylesheet">
<style>
  :root {
    --teal: #38a7a6;
    --teal-dark: #2b8786;
    --charcoal: #3a3a3c;
    --ink: #4a4a4c;
    --paper: #f3f3f3;
    --silver: #dcdcdc;
    --silver-dark: #bdbdbd;
    --white: #ffffff;
  }
  * { margin: 0; padding: 0; box-sizing: border-box; }
  html, body { width: 900px; height: 1200px; overflow: hidden; background: var(--white); }
  .flyer {
    position: relative; width: 900px; height: 1200px; overflow: hidden;
    background: linear-gradient(180deg, var(--paper) 0%, #e9e9e9 100%);
    font-family: 'Oswald', sans-serif; color: var(--ink);
  }
  .hero-art { position: absolute; left: 0; top: 0; width: 900px; height: 780px; }
  .brand {
    position: absolute; left: 48px; top: 56px;
    display: flex; align-items: center; gap: 14px;
  }
  .brand-dot { width: 22px; height: 22px; border-radius: 50%; background: var(--teal); }
  .brand-name {
    font-weight: 400; font-size: 46px; letter-spacing: 1px; color: var(--charcoal); line-height: 1;
  }
  .specials-tab { position: absolute; left: 0; top: 320px; width: 380px; height: 70px; }
  .specials-bar { position: absolute; left: 0; top: 16px; width: 380px; height: 40px; background: var(--silver); }
  .specials-circle { position: absolute; left: 46px; top: 0; width: 70px; height: 70px; border-radius: 50%; background: var(--teal); }
  .specials-label {
    position: absolute; left: 72px; top: 12px; font-weight: 600; font-size: 34px;
    letter-spacing: 2px; color: var(--white); line-height: 46px;
  }
  .special { position: absolute; left: 72px; width: 380px; }
  .special-title { font-family: 'Parisienne', cursive; font-weight: 400; font-size: 50px; color: var(--teal); line-height: 1.1; white-space: nowrap; }
  .special-desc { font-weight: 400; font-size: 17px; text-transform: uppercase; line-height: 1.3; margin-top: 6px; color: var(--ink); }
  .special-price { font-weight: 600; font-size: 38px; color: var(--charcoal); margin-top: 6px; line-height: 1; }
  .new-clients { top: 410px; }
  .elegance { top: 590px; }
  .package-band {
    position: absolute; left: 0; top: 790px; width: 900px; height: 60px; background: var(--teal);
    display: grid; grid-template-columns: repeat(3, 1fr);
  }
  .package-band h3 {
    font-family: 'Parisienne', cursive; font-weight: 400; font-size: 30px; color: var(--white);
    text-align: center; line-height: 60px; white-space: nowrap;
  }
  .packages {
    position: absolute; left: 0; top: 868px; width: 900px;
    display: grid; grid-template-columns: repeat(3, 1fr);
  }
  .package { text-align: center; }
  .package p { font-size: 17px; text-transform: uppercase; line-height: 1.3; color: var(--ink); }
  .package .special-price { margin-top: 14px; font-size: 38px; color: var(--charcoal); }
  .toner-note {
    position: absolute; left: 0; top: 1000px; width: 900px; text-align: center;
    font-size: 13px; letter-spacing: 1px; text-transform: uppercase; color: var(--ink);
  }
  .tear-line { position: absolute; left: 0; top: 1026px; width: 900px; border-top: 3px dashed var(--silver-dark); }
  .voucher {
    position: absolute; left: 0; top: 1036px; width: 900px; height: 96px; background: var(--charcoal);
    text-align: center; color: var(--white); padding-top: 8px;
  }
  .voucher-lead { font-size: 16px; letter-spacing: 1px; text-transform: uppercase; line-height: 1.3; }
  .voucher-offer { font-weight: 600; font-size: 34px; color: var(--teal); line-height: 1.1; }
  .voucher-tail { font-size: 14px; letter-spacing: 1px; text-transform: uppercase; line-height: 1.3; }
  .stores {
    position: absolute; left: 0; top: 1132px; width: 900px; height: 68px; background: var(--white);
    display: flex; justify-content: space-between; align-items: center; padding: 0 48px;
  }
  .store { font-size: 12px; line-height: 1.35; text-transform: uppercase; color: var(--ink); }
  .store strong { font-weight: 600; color: var(--teal-dark); }
  .store-right { text-align: right; }
</style>
</head>
<body>
<main class="flyer">
  <svg class="hero-art" viewBox="0 0 900 780">
    <defs>
      <linearGradient id="portraitTone" x1="0" y1="0" x2="1" y2="1">
        <stop offset="0" stop-color="#f4ead8"/>
        <stop offset="0.55" stop-color="#e3d2b4"/>
        <stop offset="1" stop-color="#cdb89a"/>
      </linearGradient>
    </defs>
    <path d="M410 0 C335 250 400 585 700 724 C790 762 860 772 900 774" fill="none" stroke="var(--silver-dark)" stroke-width="22"/>
    <path d="M440 0 C370 240 430 560 705 696 C785 732 852 744 900 748" fill="none" stroke="var(--teal)" stroke-width="26"/>
    <path role="img" aria-label="Portrait photo of a model with long, glossy platinum blonde hair"
          d="M462 0 C395 235 455 548 712 672 C790 708 856 720 900 724 L900 0 Z" fill="url(#portraitTone)"/>
  </svg>

  <header class="brand">
    <span class="brand-dot"></span>
    <span class="brand-name">Silken Tressa</span>
  </header>

  <div class="specials-tab">
    <div class="specials-bar"></div>
    <div class="specials-circle"></div>
    <div class="specials-label">SPECIALS</div>
  </div>

  <section class="special new-clients">
    <h2 class="special-title">New Clients</h2>
    <p class="special-desc">Try out Silken Tressa Studio for hair<br>cut and blow-dry</p>
    <p class="special-price">$40</p>
  </section>

  <section class="special elegance">
    <h2 class="special-title">Elegance Package</h2>
    <p class="special-desc">1/2 head of foils<br>or root-retouch, cut and blow-dry</p>
    <p class="special-price">$120*</p>
  </section>

  <div class="package-band">
    <h3>Luxurious Package</h3>
    <h3>Royal Pamper Package</h3>
    <h3>Lavish Event Package</h3>
  </div>

  <section class="packages">
    <div class="package">
      <p>Global colour, treatment,<br>cut and blow-dry</p>
      <p class="special-price">$159*</p>
    </div>
    <div class="package">
      <p>Colour, foils, treatment,<br>cut and blow-dry</p>
      <p class="special-price">$220*</p>
    </div>
    <div class="package">
      <p>Event hair styling and<br>makeup starting from</p>
      <p class="special-price">$159</p>
    </div>
  </section>

  <p class="toner-note">*Packages do not include toners</p>
  <div class="tear-line"></div>

  <section class="voucher">
    <p class="voucher-lead">Refer a friend that has not been to Silken Tressa and both receive</p>
    <p class="voucher-offer">$20 OFF</p>
    <p class="voucher-tail">Your next colour package</p>
  </section>

  <footer class="stores">
    <div class="store">
      <strong>Brenwood Store</strong><br>
      Shop 8/2 Marlowen Pde Brenwood 6091<br>
      9517 3086
    </div>
    <div class="store store-right">
      <strong>Tallowmere Store</strong><br>
      Shop 6/41 Corvella Dunes Ave Tallowmere 6094<br>
      9538 2470
    </div>
  </footer>
</main>
</body>
</html>
```